Re-Design an adult education portal

I need support to re-design an adult education portal. Currently the customer has an incomplete website which should be prepared in a new format.
I have the idea how to realize, but I have no clue how to design it. The hard thing is to have a "beautiful" website with available logo and main color. I hope you can support me.

Name of Website: tovrenu (tovrenu.ch)
Content: adult eduction for adult in safety at work, mountain climbing, dog school. various courses in different areas. But on old webpage is hard to find the different possibilities.
main color: Ral 6011 (green) -> #6C7C59
logo: you see on top of website the logo (2 dogs and a mountain with a colour gradient).

new website: for new webpage I decided to have a navigation for each section of education. In the main area I would like to have some pictures to give an idea what content is behind. At the moment it looks terrible, so I decided to use you as support for me to make the webpage prettier :). And maybe you have an better idea how to make it great. -> current state of new web page: https://tovrenu.bask-om.ch/

Target Market(s)

adult eduction for adult in safety at work, mountain climbing, dog school

Number of Pages Required

1 page

Font styles to use
Serif
Sans Serif

Requirements
Must have
• As main color is set "Ral 6011" (green) -> #6C7C59

```html
<!DOCTYPE html>
<html lang="de">
<head>
<meta charset="utf-8">
<title>tovrenu – Ihr Ausbildungs- und Kurspartner</title>
<link rel="stylesheet" href="https://fonts.googleapis.com/css2?family=Arimo:wght@400;700&family=Tinos:wght@400&display=swap">
<style>
:root{
  --olive:#5f5e25;
  --olive-dark:#4d4c1c;
  --brand:#6C7C59;
  --text:#333333;
  --muted:#555555;
  --light:#f4f4f4;
  --footer:#232323;
  --footer-bottom:#1a1a1a;
  --white:#ffffff;
}
*{margin:0;padding:0;box-sizing:border-box}
html,body{width:1200px;height:3886px;overflow:hidden;background:var(--white)}
body{position:relative;font-family:"Arimo",Arial,sans-serif;color:var(--text)}
.abs{position:absolute}

/* header */
.site-header{position:absolute;left:0;top:0;width:1200px;height:122px;background:var(--white)}
.brand{position:absolute;left:100px;top:22px;width:236px;height:78px;display:flex;align-items:center;gap:12px}
.brand-mark{width:30px;height:30px;border-radius:50%;background:var(--brand)}
.brand-name{font-size:34px;font-weight:400;color:var(--olive)}
.top-contact{position:absolute;top:22px;display:flex;align-items:center;gap:12px;font-size:14px;color:#555}
.icon-dot{width:26px;height:26px;border-radius:50%;background:var(--olive);display:flex;align-items:center;justify-content:center}
.main-nav{position:absolute;top:78px;left:449px;display:flex;gap:0;font-size:15px}
.main-nav a{color:#222;text-decoration:none;margin-right:22px;position:relative;height:44px}
.main-nav a.active{color:#888}
.main-nav a.active::after{content:"";position:absolute;left:0;right:0;bottom:0;height:2px;background:var(--olive)}

/* hero */
.hero{position:absolute;left:0;top:122px;width:1200px;height:537px;
  background:linear-gradient(160deg,#28406e 0%,#3c4a5c 35%,#5a4a3c 65%,#2d2620 100%)}
.hero-title{position:absolute;left:98px;top:168px;color:var(--white);font-weight:700;line-height:1.08;text-shadow:0 2px 6px rgba(0,0,0,.35)}
.hero-title .l1{display:block;font-size:60px}
.hero-title .l2{display:block;font-size:46px}
.hero-dots{position:absolute;left:102px;top:360px;display:flex;gap:9px;align-items:center}
.hero-dots span{width:11px;height:11px;border-radius:50%;background:var(--white)}
.hero-dots span.on{width:18px;height:18px;background:transparent;border:2px solid var(--white);position:relative}
.hero-dots span.on::after{content:"";position:absolute;left:3px;top:3px;width:8px;height:8px;border-radius:50%;background:var(--white)}

/* intro */
.intro-title{position:absolute;left:0;width:1200px;top:710px;text-align:center;font-size:34px;font-weight:700;color:#333}
.intro-sub{position:absolute;left:0;width:1200px;top:772px;text-align:center;font-size:15px;color:#444}
.intro-photo{position:absolute;left:117px;top:833px;width:477px;height:295px;border:1px solid #ddd;padding:4px;background:var(--white)}
.intro-photo div{width:100%;height:100%;background:linear-gradient(180deg,#a9c4d8 0%,#d9e5ee 55%,#f2f4f6 100%)}
.intro-copy{position:absolute;left:626px;top:830px;width:460px;font-size:11.2px;line-height:22px;color:#444}
.intro-copy ul{list-style:none;margin-top:24px;padding-left:3px}
.btn-solid{position:absolute;display:flex;align-items:center;justify-content:center;background:var(--olive);color:var(--white);font-weight:700;font-size:13.5px;border-radius:18px}

/* feature bands */
.band{position:absolute;left:0;width:1200px;height:416px;background:var(--light)}
.band svg{position:absolute;left:0;top:0}
.band-title{position:absolute;font-size:34px;font-weight:700;color:#3a3a3a}
.band-list{position:absolute;list-style:none;font-size:11px;line-height:20.5px;color:#555}
.band-list li{padding-left:17px;position:relative}
.band-list li::before{content:"";position:absolute;left:0;top:8px;width:5px;height:5px;border-radius:50%;background:#aaa}
.btn-outline{position:absolute;width:106px;height:30px;border:1px solid #555;border-radius:15px;display:flex;align-items:center;justify-content:center;gap:4px;font-size:10px;color:#333;background:var(--white)}
.btn-outline i{width:9px;height:9px;border:1.5px solid #333;border-radius:50%;display:inline-block}

/* CZV grid */
.section-title{position:absolute;left:0;width:1200px;text-align:center;font-weight:700;color:#333}
.section-rule{position:absolute;left:570px;width:60px;height:3px;background:var(--olive)}
.tile{position:absolute;width:397px;height:260px;display:flex;flex-direction:column;align-items:center;justify-content:center;color:var(--white);text-align:center}
.tile h3{font-size:20px;font-weight:700;letter-spacing:.3px;text-shadow:0 1px 4px rgba(0,0,0,.5)}
.tile p{font-size:10.5px;line-height:30px;text-transform:uppercase}

/* team */
.team{position:absolute;left:0;top:3083px;width:1200px;height:395px;background:linear-gradient(180deg,#f3f3f1 0%,#fafaf9 60%,#ededeb 100%)}
.member-photo{position:absolute;width:121px;height:121px;border-radius:50%}
.member-quote{position:absolute;width:290px;font-family:"Tinos",serif;font-size:11.5px;line-height:21px;color:#555}
.member-name{position:absolute;font-family:"Tinos",serif;font-size:12.5px;line-height:22px;color:var(--olive)}
.quote-mark{position:absolute;font-family:"Tinos",serif;font-size:78px;color:#c9c9c9;line-height:1}

/* footer */
.site-footer{position:absolute;left:0;top:3478px;width:1200px;height:342px;background:var(--footer);color:var(--white)}
.footer-logo{position:absolute;left:103px;top:127px;width:153px;height:83px;background:var(--white);display:flex;align-items:center;justify-content:center;gap:8px}
.footer-logo .brand-name{font-size:24px}
.footer-logo .brand-mark{width:18px;height:18px}
.footer-h{position:absolute;font-size:19.5px;font-weight:700;letter-spacing:.3px}
.footer-line{position:absolute;display:flex;align-items:flex-start;gap:12px;font-size:12.5px;line-height:20px}
.socials{position:absolute;left:314px;top:246px;display:flex;gap:4px}
.socials span{width:22px;height:22px;border:1px solid #aaa;border-radius:50%}
.field{position:absolute;border:1px solid #bbb;font-size:11px;color:#ddd;padding:16px 14px}
.submit{position:absolute;left:873px;top:219px;width:225px;height:42px;background:var(--olive);display:flex;align-items:center;justify-content:center;font-weight:700;font-size:13px}
.footer-bottom{position:absolute;left:0;top:3820px;width:1200px;height:66px;background:var(--footer-bottom);color:#ddd;font-size:11.5px;display:flex;align-items:center;justify-content:center}
</style>
</head>
<body>

<header class="site-header">
  <div class="brand"><span class="brand-mark"></span><span class="brand-name">tovrenu.ch</span></div>
  <div class="top-contact" style="left:792px">
    <span class="icon-dot"><svg width="13" height="13" viewBox="0 0 24 24"><path fill="#fff" d="M6.6 10.8a15 15 0 0 0 6.6 6.6l2.2-2.2c.3-.3.7-.4 1-.2 1.1.4 2.3.6 3.6.6.6 0 1 .4 1 1V20c0 .6-.4 1-1 1A17 17 0 0 1 3 4c0-.6.4-1 1-1h3.5c.6 0 1 .4 1 1 0 1.3.2 2.5.6 3.6.1.3 0 .7-.2 1z"/></svg></span>
    <span>+41 79 555 01 23</span>
  </div>
  <div class="top-contact" style="left:968px">
    <span class="icon-dot"><svg width="13" height="13" viewBox="0 0 24 24"><rect x="3" y="6" width="18" height="12" rx="1" fill="none" stroke="#fff" stroke-width="2"/><path d="M3 7l9 6 9-6" fill="none" stroke="#fff" stroke-width="2"/></svg></span>
    <span>info@tovrenu.ch</span>
  </div>
  <nav class="main-nav">
    <a class="active">Home</a><a>Arbeitssicherheit</a><a>Erste Hilfe</a><a>Hundeschule</a><a>CZV</a><a>Bergausbildung</a><a>Tovrenu</a>
  </nav>
</header>

<section class="hero" role="img" aria-label="Photo of the two instructors sitting outdoors with their dogs under trees">
  <h1 class="hero-title"><span class="l1">IHR AUSBILDUNGS-</span><span class="l2">UND KURSPARTNER</span></h1>
  <div class="hero-dots"><span class="on"></span><span></span><span></span><span></span></div>
</section>

<h2 class="intro-title">Ihr Ausbildungs- und Kurspartner</h2>
<p class="intro-sub">Wir bieten Ihren Wünschen entsprechende Ausbildungen, zielorientiert und Ihrem Können und Wissen angepasst.</p>
<div class="intro-photo"><div role="img" aria-label="Photo of a person standing on top of a ladder against a cloudy sky"></div></div>
<div class="intro-copy">
  <p>Hubarbeitsbühnen sind ein Effizientes Arbeitsmittel. Bediener müssen sorgfältig ausgewählt werden und benötigen eine gezielte Ausbildung. Der Arbeitgeber ist verantwortlich für die Auswahl und die Ausbildung der Personen welche diese Arbeiten auszuführen.</p>
  <ul>
    <li>Gute Deutschkenntnisse und gutes Auffassungsvermögen</li>
    <li>Körperliche und geistige Gesundheit</li>
    <li>Keine Höhenangst</li>
    <li>Technisches Verständnis ist vorhanden</li>
    <li>Zuverlässige, verantwortungsbewusste und umsichtige Handlungsweise ist wahrnehmbar</li>
  </ul>
</div>
<div class="btn-solid" style="left:626px;top:1075px;width:155px;height:36px">LEARN MORE</div>

<section class="band" style="top:1180px">
  <svg width="1200" height="416" role="img" aria-label="Photo of climbers on a rocky mountain ridge with helmets">
    <defs><linearGradient id="gClimb" x1="0" y1="0" x2="0" y2="1"><stop offset="0" stop-color="#7e98b8"/><stop offset=".45" stop-color="#8a8f8a"/><stop offset="1" stop-color="#4f5640"/></linearGradient></defs>
    <path d="M0 0H575C545 130 535 280 575 416H0Z" fill="url(#gClimb)"/>
    <path d="M575 0C545 130 535 280 575 416" fill="none" stroke="var(--olive)" stroke-width="4"/>
  </svg>
  <h2 class="band-title" style="left:636px;top:95px">Kursinhalt</h2>
  <ul class="band-list" style="left:658px;top:160px">
    <li>Fachgerechte Übernahme und Inbetriebsetzung von Hebebühnen</li>
    <li>Geräte Aufbau, Funktionen und Einsatzmöglichkeiten</li>
    <li>Arbeitssicherheit – Gefahrenpotential</li>
    <li>Pflichten – Verantwortung</li>
    <li>Sicherung von Baustellen</li>
  </ul>
  <div class="btn-outline" style="left:636px;top:293px">READ MORE <i></i></div>
</section>

<section class="band" style="top:1597px">
  <svg width="1200" height="416" role="img" aria-label="Photo of a black driving-school truck on a country road">
    <defs><linearGradient id="gTruck" x1="0" y1="0" x2="0" y2="1"><stop offset="0" stop-color="#8fb3e0"/><stop offset=".4" stop-color="#3b3e3a"/><stop offset=".75" stop-color="#6f8f45"/><stop offset="1" stop-color="#5a5a55"/></linearGradient></defs>
    <path d="M1200 0H575C545 130 545 280 560 416H1200Z" fill="url(#gTruck)"/>
    <path d="M575 0C545 130 545 280 560 416" fill="none" stroke="var(--olive)" stroke-width="4"/>
  </svg>
  <h2 class="band-title" style="left:96px;top:95px">Grundausbildung</h2>
  <ul class="band-list" style="left:120px;top:160px">
    <li>Theoretische Ausbildung mit schriftlicher Prüfung</li>
    <li>Praxisschulung an entsprechenden Gerätetypen mit praktischer Prüfung</li>
    <li>Theoretische Ausbildung mit schriftlicher Prüfung</li>
  </ul>
  <div class="btn-outline" style="left:96px;top:279px">READ MORE <i></i></div>
</section>

<section class="band" style="top:2014px">
  <svg width="1200" height="416" role="img" aria-label="Photo of a regional passenger train on tracks through green fields">
    <defs><linearGradient id="gTrain" x1="0" y1="0" x2="0" y2="1"><stop offset="0" stop-color="#d9e2ea"/><stop offset=".45" stop-color="#c7cfc2"/><stop offset=".75" stop-color="#6e8d3a"/><stop offset="1" stop-color="#5b5448"/></linearGradient></defs>
    <path d="M0 0H575C545 130 535 280 575 416H0Z" fill="url(#gTrain)"/>
    <path d="M575 0C545 130 535 280 575 416" fill="none" stroke="var(--olive)" stroke-width="4"/>
  </svg>
  <h2 class="band-title" style="left:636px;top:78px">Zertifikate</h2>
  <ul class="band-list" style="left:658px;top:124px">
    <li>VHAB Bediener Ausweis</li>
    <li>( Verband Helvetischer Arbeitsbühnen Betriebe )</li>
    <li>VUKA anerkannt</li>
    <li>Gültigkeit; Lebenslänglich</li>
    <li>CZV anerkannt auf verlangen</li>
  </ul>
  <div class="btn-outline" style="left:636px;top:256px">READ MORE <i></i></div>
</section>

<h2 class="section-title" style="top:2465px;font-size:32px">CZV</h2>
<div class="section-rule" style="top:2510px"></div>

<div class="tile" style="left:0;top:2545px;background:linear-gradient(135deg,#cfcfcf,#b23a30 60%,#2a2a2a)" role="img" aria-label="Photo of a red forklift"><h3>STAPLERKURSE</h3></div>
<div class="tile" style="left:402px;top:2545px;background:linear-gradient(135deg,#b8ae74,#a0995e 50%,#8d8350)" role="img" aria-label="Photo of coiled safety ropes"><h3>PSAGA</h3><p>Persönliche Schutzausrüstung<br>gegen Absturz (PSAGA)</p></div>
<div class="tile" style="left:804px;top:2545px;background:linear-gradient(180deg,#7fa3cf,#6f7a6a 55%,#55513f)" role="img" aria-label="Photo of an orange aerial work platform next to a large barrel"><h3>HUBARBEITSBÜHNE</h3></div>
<div class="tile" style="left:0;top:2810px;background:linear-gradient(180deg,#49523a,#3a3528 55%,#4d6a2c)" role="img" aria-label="Photo of three dogs lying in a forest clearing"><h3>HUNDESCHULE</h3></div>
<div class="tile" style="left:402px;top:2810px;background:linear-gradient(180deg,#7d7f86,#8c8f96 50%,#a49c92)" role="img" aria-label="Photo of a first aid resuscitation training session"><h3>NOTHELFER</h3></div>
<div class="tile" style="left:804px;top:2810px;background:linear-gradient(135deg,#6e6e70,#767677 60%,#6a5a5a)" role="img" aria-label="Red sanitation training emblem on grey background"><h3>SANITÄTSSCHULUNG</h3></div>

<section class="team">
  <h2 class="section-title" style="top:68px;font-size:32px">OUR TEAM</h2>
  <div class="section-rule" style="top:122px"></div>

  <div class="member-photo" style="left:94px;top:178px;background:radial-gradient(circle at 50% 40%,#9cb8d6,#3f5f86)" role="img" aria-label="Portrait photo of mountain guide Lukas Ammeter"></div>
  <p class="member-quote" style="left:236px;top:184px">“ Ausbildner Bergbahnen Alpenland Lawinenhundeführer &amp; Ausbildner KNRO Nothilfeinstruktor (Société Alpine de Contrôle)</p>
  <p class="member-name" style="left:236px;top:260px">Lukas Ammeter-<br>Dipl. Bergführer &amp; dipl. Schneesportlehrer</p>
  <span class="quote-mark" style="left:528px;top:248px">”</span>

  <div class="member-photo" style="left:633px;top:178px;background:radial-gradient(circle at 50% 45%,#d36a2a,#2f4f7a)" role="img" aria-label="Portrait photo of mountain guide Sonja Ammeter with arms raised on a summit"></div>
  <p class="member-quote" style="left:775px;top:184px">“ Ausbildner Bergbahnen Alpenland Lawinenhundeführer &amp; Ausbildner KNRO Nothilfeinstruktor (Société Alpine de Contrôle)</p>
  <p class="member-name" style="left:775px;top:260px">Sonja Ammeter-<br>Dipl. Bergführer &amp; dipl. Schneesportlehrer</p>
  <span class="quote-mark" style="left:1058px;top:248px">”</span>
</section>

<footer class="site-footer">
  <div class="footer-logo"><span class="brand-mark"></span><span class="brand-name">tovrenu.ch</span></div>
  <h3 class="footer-h" style="left:312px;top:72px">CONTACT US</h3>
  <div class="footer-line" style="left:312px;top:124px">
    <svg width="14" height="16" viewBox="0 0 24 24" style="margin-top:4px"><path fill="#fff" d="M12 2a7 7 0 0 0-7 7c0 5 7 13 7 13s7-8 7-13a7 7 0 0 0-7-7zm0 9.5A2.5 2.5 0 1 1 12 6.5a2.5 2.5 0 0 1 0 5z"/></svg>
    <span>Talstrasse 48,<br>CH-3905 Ortsberg</span>
  </div>
  <div class="footer-line" style="left:312px;top:181px">
    <svg width="14" height="14" viewBox="0 0 24 24" style="margin-top:3px"><path fill="#fff" d="M6.6 10.8a15 15 0 0 0 6.6 6.6l2.2-2.2c.3-.3.7-.4 1-.2 1.1.4 2.3.6 3.6.6.6 0 1 .4 1 1V20c0 .6-.4 1-1 1A17 17 0 0 1 3 4c0-.6.4-1 1-1h3.5c.6 0 1 .4 1 1 0 1.3.2 2.5.6 3.6.1.3 0 .7-.2 1z"/></svg>
    <span>Telefon: +41 79 555 01 23</span>
  </div>
  <div class="footer-line" style="left:312px;top:212px;font-size:11.5px">
    <svg width="14" height="14" viewBox="0 0 24 24" style="margin-top:3px"><rect x="3" y="6" width="18" height="12" fill="#fff"/><path d="M3 6l9 6 9-6" fill="none" stroke="#232323" stroke-width="2"/></svg>
    <span>E-Mail: info@tovrenu.ch</span>
  </div>
  <div class="socials"><span></span><span></span><span></span><span></span></div>

  <h3 class="footer-h" style="left:630px;top:72px">GET A QUOTE</h3>
  <p class="abs" style="left:630px;top:117px;width:470px;font-size:11px;line-height:19px">Wir bieten Ihren Wünschen entsprechende Ausbildungen, zielorientiert und Ihrem Können und Wissen angepasst.</p>
  <div class="field" style="left:630px;top:167px;width:233px;height:42px;padding:13px 14px;font-size:10px">Name</div>
  <div class="field" style="left:870px;top:167px;width:228px;height:42px;padding:13px 14px;font-size:10px">E - Mail</div>
  <div class="field" style="left:630px;top:219px;width:233px;height:43px;padding:13px 14px;font-size:13px">Telefon</div>
  <div class="submit">SUBMIT NOW!</div>
</footer>
<div class="footer-bottom">© 2021 tovrenu . All Rights Reserved.</div>

</body>
</html>
```